A Spinner Of Grace Company Brochure

I am the owner of a Mobile Disc Jockey company specializing in weddings. I am looking for a Tri Fold color brochure that is modern and eye catching with the focus being on upscale wedding events. I also want it to be easy to read and not overly cluttered ! I would like it to reflect our website located at aspinnerofgrace.example
I also have different variations and file types of my logo such as jpeg and png files. I need some good dance floor pics. If you do not have any good stock photos I can look through my photo library. I uploaded a logo and pic I found from one of my videos. Not sure if it is worth anything.
We also do Uplighting and Photo Booths which I would like in the brochure. Much of the text copy needed can be taken from our website if needed. Please refer to the website to see what we do and our style.

Target Market(s)

upscale weddings

Industry/Entity Type

wedding dj entertainment & masters of ceremonies

Requirements
Nice to have
• nice pictures of packed dance floors and people having fun

```html
<!DOCTYPE html>
<html lang="en">
<head>
<meta charset="utf-8">
<title>A Spinner Of Grace – Tri-Fold Brochure</title>
<link rel="stylesheet" href="https://fonts.googleapis.com/css2?family=Oswald:wght@500&family=Cinzel:wght@500&family=Questrial&family=Arimo:wght@400;700&family=Tinos&display=swap">
<style>
:root{
  --purple:#7c3b97;
  --purple-dark:#5d2777;
  --purple-deep:#3d1a4f;
  --pink:#e5175a;
  --pink-soft:#f2a5bd;
  --ink:#333;
  --grey:#5a5a5a;
  --paper:#fff;
  --bg:#ececec;
}
*{box-sizing:border-box;margin:0;padding:0}
html,body{width:1200px;height:2941px;overflow:hidden;background:var(--bg)}
body{position:relative;font-family:"Arimo",Arial,sans-serif;color:var(--ink)}
.spread{position:absolute;left:98px;width:1004px;height:776px;overflow:hidden;box-shadow:0 6px 18px rgba(0,0,0,.25)}
.spread--outside{top:560px;background:var(--paper)}
.spread--inside{top:1500px;background:var(--purple)}
.abs{position:absolute}
.photo{position:absolute}

/* outside – services panel */
.services{left:0;top:0;width:339px;height:776px;background:var(--purple)}
.services__title{left:40px;top:26px;font-family:"Cinzel",serif;font-size:25px;line-height:24px;color:#fff;letter-spacing:.5px}
.tile{position:absolute;left:38px;width:258px;height:107px}
.tile__label{position:absolute;left:0;top:0;width:100%;height:22px;background:linear-gradient(90deg,#c8124a,var(--pink),#c8124a);color:#fff;font-family:"Tinos",serif;font-size:15px;text-align:center;line-height:22px;z-index:1}
.tile__photo{position:absolute;inset:0}

/* outside – middle panel */
.reviews{left:339px;top:0;width:327px;height:219px;background:#fff}
.review{position:absolute;left:0;width:327px;text-align:center}
.review__text{font-size:11px;line-height:14px;color:var(--ink)}
.review__name{font-size:12px;font-weight:700;color:var(--pink);margin-top:4px}
.review__rule{position:absolute;top:50px;width:60px;border-top:1px solid #ccc}
.quote{position:absolute;font-family:"Tinos",serif;font-size:46px;color:var(--pink-soft);line-height:1}
.feed{left:54px;top:171px;display:flex;align-items:center;gap:10px}
.feed__icon{width:26px;height:26px;border-radius:6px;background:var(--purple)}
.feed__text{font-size:15px;line-height:15px;color:var(--ink)}
.feed__text b{color:var(--pink)}
.band{left:339px;top:219px;width:327px;height:60px}
.mid-photo{left:332px;top:276px;width:334px;height:198px;background:linear-gradient(135deg,#2c1d20,#8a6f66 45%,#d9cfc8 60%,#3b2a2a)}

/* outside – cover panel */
.cover-logo{left:666px;top:0;width:338px;height:116px;background:#fff;display:flex;align-items:center;justify-content:center;gap:10px}
.cover-logo__dot{width:18px;height:18px;border-radius:50%;background:var(--purple)}
.cover-logo__name{font-family:"Oswald",sans-serif;font-size:30px;color:#666}
.cover-photo{left:666px;top:116px;width:338px;height:358px;background:radial-gradient(circle at 45% 25%,#d8d3e8,#5b4f78 30%,#1f1a24 70%)}
.strip{left:332px;top:474px;width:672px;height:17px;background:var(--purple)}

/* outside – contact */
.contact{left:339px;top:491px;width:665px;height:285px;background:#fff}
.join{left:22px;top:26px;width:265px;text-align:center;font-size:13px;font-weight:700;line-height:16px}
.join em{font-style:normal;color:var(--pink)}
.dots{left:143px;top:62px;font-size:8px;color:#aaa;letter-spacing:2px}
.remember{left:25px;top:76px;font-size:10px;color:var(--grey)}
.pill{display:inline-block;background:var(--purple);color:#fff;font-size:12px;border-radius:10px;padding:2px 8px}
.contact__pill{left:24px;top:110px}
.contact__list{left:22px;top:140px;list-style:none}
.contact__list li{display:flex;align-items:center;gap:8px;height:25px;font-size:10px;color:var(--ink)}
.contact__list li.phone{font-size:17px;font-weight:700;color:var(--pink)}
.contact__list b{color:var(--pink)}
.ic{width:19px;height:19px;border-radius:50%;background:var(--purple);display:flex;align-items:center;justify-content:center;flex:none}
.corner{left:561px;top:0;width:104px;height:37px}
.motto{left:355px;top:65px;width:300px}
.motto__line{font-family:"Oswald",sans-serif;font-size:36px;line-height:38px;letter-spacing:-.5px;color:#7d7d7d}
.motto__line--accent{color:var(--purple)}
.motto__tag{font-size:11px;font-weight:700;color:#444;margin-top:2px}
.call{left:391px;top:185px;width:207px;height:48px;border:1px solid #999;text-align:center}
.call__label{position:absolute;left:50%;top:-9px;transform:translateX(-50%);background:#fff;border:1px solid var(--pink);border-radius:8px;padding:0 7px;font-family:"Tinos",serif;font-size:12px;color:var(--pink);white-space:nowrap}
.call__number{font-size:27px;line-height:48px;color:#333}
.url{left:401px;top:242px;width:166px;height:19px;border-radius:10px;background:var(--purple);color:#fff;font-size:11px;font-weight:700;text-align:center;line-height:19px}

/* inside */
.hero{left:0;top:0;width:1004px;height:343px;background:linear-gradient(90deg,#4a3a48,#6e5c6a 25%,#3a2a3e 55%,#7a6055 80%,#3a2c35)}
.snap{position:absolute;border:5px solid #fff;box-shadow:0 2px 6px rgba(0,0,0,.45)}
.heading{font-family:"Cinzel",serif;font-size:33px;color:#fff;letter-spacing:.5px}
.ticks{list-style:none}
.ticks li{position:relative;padding-left:31px;font-family:"Questrial",sans-serif;font-size:21px;line-height:28px;color:#fff}
.ticks li::before{content:"";position:absolute;left:0;top:8px;width:13px;height:13px;border-radius:50%;background:#fff}
.ticks li::after{content:"";position:absolute;left:4px;top:11px;width:3px;height:5px;border:solid var(--purple);border-width:0 2px 2px 0;transform:rotate(45deg)}
.thumb{position:absolute;width:140px;height:128px;border:4px solid #fff}
.booth-intro{left:358px;top:419px;width:270px;font-size:11px;font-weight:700;line-height:13px;color:#fff}
</style>
</head>
<body>

<!-- OUTSIDE SPREAD -->
<section class="spread spread--outside" aria-label="Brochure outside spread">

  <div class="abs services">
    <h2 class="abs services__title">SOCIAL EVENTS<br>PRIVATE PARTIES</h2>
    <div class="tile" style="top:80px"><div class="tile__label">Country Club Events</div><div class="tile__photo" role="img" aria-label="Guests laughing at a country club party" style="background:linear-gradient(90deg,#e9e2d8,#b89a82 50%,#6a5248)"></div></div>
    <div class="tile" style="top:198px"><div class="tile__label">Life Celebrations Parties</div><div class="tile__photo" role="img" aria-label="Friends celebrating a birthday" style="background:linear-gradient(90deg,#3a2c2c,#c9b2a4 45%,#4a3a3a)"></div></div>
    <div class="tile" style="top:316px"><div class="tile__label">Fashion Shows Fund Raisers</div><div class="tile__photo" role="img" aria-label="Runway fashion show in a ballroom" style="background:linear-gradient(180deg,#5a5f8a,#2b3050)"></div></div>
    <div class="tile" style="top:434px"><div class="tile__label">Social Photo Booth</div><div class="tile__photo" role="img" aria-label="Guests posing at a teal-lit photo booth" style="background:linear-gradient(90deg,#0a3f44,#27b9b0 55%,#0c2e33)"></div></div>
    <div class="tile" style="top:552px"><div class="tile__label">Karaoke</div><div class="tile__photo" role="img" aria-label="Group singing karaoke together" style="background:linear-gradient(90deg,#c9a07e,#e8d3bd 50%,#8a5e48)"></div></div>
    <div class="tile" style="top:670px;height:106px"><div class="tile__label">Game Shows</div><div class="tile__photo" role="img" aria-label="Colourful game show score boards" style="background:linear-gradient(90deg,#e9eef2,#b7d7a8 40%,#c3b5e0 75%,#e9eef2)"></div></div>
  </div>

  <div class="abs reviews">
    <div class="quote" style="left:48px;top:26px">“</div>
    <div class="quote" style="left:236px;top:26px">”</div>
    <div class="review" style="top:34px"><p class="review__text">Fantastic experience,<br>highly recommend!</p><p class="review__name">BRIANNA</p></div>
    <div class="quote" style="left:48px;top:88px">“</div>
    <div class="quote" style="left:236px;top:88px">”</div>
    <div class="review" style="top:97px"><p class="review__text">DJ Theo had everyone the<br>dance floor the whole night!</p><p class="review__name">LENA</p></div>
    <div class="abs feed"><span class="feed__icon"></span><p class="feed__text">CHECK US OUT ON<br><b>PHOTO FEED</b></p></div>
  </div>
  <svg class="abs band" viewBox="0 0 327 60" aria-hidden="true"><polygon points="0,0 327,0 327,60 130,60 112,38 0,38" fill="var(--purple)"/></svg>
  <div class="photo mid-photo" role="img" aria-label="Smiling guests dancing at a party"></div>

  <div class="abs cover-logo"><span class="cover-logo__dot"></span><span class="cover-logo__name">A Spinner Of Grace</span></div>
  <div class="photo cover-photo" role="img" aria-label="Crowd with raised hands under stage lights"></div>
  <div class="abs strip"></div>

  <div class="abs contact">
    <p class="abs join">Join Over <em>1,000 Happy</em> Customers that have enjoyed A Spinner Of Grace</p>
    <span class="abs dots">• • • • •</span>
    <p class="abs remember">Have your event be remembered as being one of the greats</p>
    <span class="abs pill contact__pill">CONTACT US</span>
    <ul class="abs contact__list">
      <li><span class="ic"><svg width="10" height="12" viewBox="0 0 10 12"><path d="M5 0a4 4 0 0 1 4 4c0 3-4 8-4 8S1 7 1 4a4 4 0 0 1 4-4z" fill="#fff"/><circle cx="5" cy="4" r="1.5" fill="var(--purple)"/></svg></span>A Spinner Of Grace Palm Cove, FL 30012</li>
      <li class="phone"><span class="ic"><svg width="11" height="11" viewBox="0 0 11 11"><path d="M2 0l2 2.5-1 1.5a7 7 0 0 0 3.5 3.5L8 6.5 11 9l-1.5 2C4.5 11 0 6.5 0 1.5z" fill="#fff"/></svg></span>555.014.2290</li>
      <li><span class="ic"><svg width="11" height="8" viewBox="0 0 11 8"><rect width="11" height="8" fill="#fff"/><path d="M0 0l5.5 4.5L11 0" fill="none" stroke="var(--purple)"/></svg></span>info@aspinnerofgrace.example</li>
      <li><span class="ic"><svg width="11" height="11" viewBox="0 0 11 11"><circle cx="5.5" cy="5.5" r="4.5" fill="none" stroke="#fff"/><path d="M1 5.5h9M5.5 1v9" stroke="#fff"/></svg></span>www.<b>aspinnerofgrace</b>.example</li>
      <li><span class="ic"><svg width="11" height="11" viewBox="0 0 11 11"><circle cx="5.5" cy="5.5" r="4.5" fill="none" stroke="#fff"/><path d="M5.5 2.5v3h2" fill="none" stroke="#fff"/></svg></span>Monday - Friday: 8:00 AM - 10:00 PM</li>
    </ul>
    <svg class="abs corner" viewBox="0 0 104 37" aria-hidden="true"><polygon points="0,0 104,0 104,37 12,37" fill="var(--purple)"/></svg>
    <div class="abs motto">
      <p class="motto__line">MODERN TASTEFUL</p>
      <p class="motto__line motto__line--accent">&amp; FUN ENTERTAINMENT</p>
      <p class="motto__tag">ANY EVENT IS BETTER WITH A SPINNER OF GRACE</p>
    </div>
    <div class="abs call"><span class="call__label">CALL US TODAY</span><p class="call__number">(555) 014 2290</p></div>
    <p class="abs url">www.aspinnerofgrace.example</p>
  </div>
</section>

<!-- INSIDE SPREAD -->
<section class="spread spread--inside" aria-label="Brochure inside spread">
  <div class="photo hero" role="img" aria-label="Bride lifted by guests and couple dancing through confetti"></div>
  <div class="snap" style="left:384px;top:30px;width:240px;height:160px;transform:rotate(-3deg);background:linear-gradient(#3c4a7a,#1e2440)" role="img" aria-label="Packed ballroom dance floor"></div>
  <div class="snap" style="left:290px;top:132px;width:160px;height:190px;transform:rotate(-7deg);background:linear-gradient(135deg,#0d3b40,#2fb6ad,#0d3b40)" role="img" aria-label="Guests dancing under teal light"></div>
  <div class="snap" style="left:512px;top:132px;width:150px;height:180px;transform:rotate(6deg);background:linear-gradient(135deg,#4a3434,#c9a48f,#3a2a2a)" role="img" aria-label="Women laughing on the dance floor"></div>

  <div class="abs" style="left:29px;top:368px">
    <h2 class="heading">WEDDINGS</h2>
    <ul class="ticks" style="margin-top:10px">
      <li>Wedding Ceremonies</li><li>DJ Entertainment</li><li>Lighting</li><li>Photo Booth</li><li>Dancing on Clouds</li><li>Monogram Lighting</li>
    </ul>
  </div>
  <div class="thumb" style="left:26px;top:613px;background:linear-gradient(#3f4f80,#22284a)" role="img" aria-label="Uplit ballroom reception"></div>
  <div class="thumb" style="left:176px;top:613px;background:linear-gradient(#6a7a4a,#c9c0a0)" role="img" aria-label="Costumed performer at a reception"></div>

  <h2 class="abs heading" style="left:356px;top:370px">PHOTO-BOOTH</h2>
  <p class="abs booth-intro">Add more fun and excitement to your event with our photo booth. We offer several back drops and props!</p>
  <div class="thumb" style="left:358px;top:470px;width:272px;height:274px;background:linear-gradient(135deg,#d9d9d9,#8a7a6a 40%,#c8c060 70%,#444)" role="img" aria-label="Guests posing with photo booth props and signs"></div>

  <div class="thumb" style="left:673px;top:375px;background:linear-gradient(#3f4f80,#22284a)" role="img" aria-label="Corporate banquet hall"></div>
  <div class="thumb" style="left:824px;top:375px;background:linear-gradient(#6a7a4a,#c9c0a0)" role="img" aria-label="Performer at a corporate gala"></div>
  <div class="abs" style="left:686px;top:534px">
    <h2 class="heading">CORPORATE</h2>
    <ul class="ticks" style="margin-top:16px">
      <li>DJ Entertainment</li><li>Lighting</li><li>Branding</li><li>Photo Booth</li><li>Game Shows</li><li>Karaoke</li>
    </ul>
  </div>
</section>

</body>
</html>
```